Lumavault Web Design Project

We need a new web page for our startup company based in San Jose, CA called Lumavault.
Lumavault is a web application that helps small businesses share confidential information with their employees, customers, and partners.
With Lumavault, you can share files, bookmarks, and videos on a 'custom' web page that has your logo and that you can host on your servers or on ours. We allow our customers to maintain control of the user experience during sharing by sharing online without sending users to a third-party branded site such as stackpail, crate.io or Orbis cache. Lumavault notifies you know when someone views your content and allows you to recall shared items and email anytime.

"Lumavault can be likened to a secure stackpail with visibility and control of the user experience and on the content that is shared"

We would like to see designs that uses green and black as in the colors on our website www.lumavault.example.
The final design should communicate:
* Secure, Gives Control, Fast, Reliable, Safe, Simple, Flexible, Connects from any device, empower, works on mobile, anywhere, and helpful.

Target Market(s)

Accountants, Financial Advisors, Small Businesses, Start up companies that need to share confidential information online

Industry/Entity Type

It Company

Font styles to use
Sans Serif

Requirements
Must have
• tells customers that they can customize the cloud experience for their users and that they can share online with confidence. Design must be responsive - i.e. should automatically resize itself for viewing on mobile devices
Should not have
• Show secure concept without using a lock image. we feel that lock is old school and does not necessarily show flexibility - we would like to show flexibility with control

```html
<!DOCTYPE html>
<html lang="en">
<head>
<meta charset="utf-8">
<title>Lumavault – share online with confidence</title>
<link rel="stylesheet" href="https://fonts.googleapis.com/css2?family=Open+Sans:wght@400;600;700&family=Ubuntu:wght@400;500&display=swap">
<style>
:root{
  --teal:#2f9cac;
  --teal-dark:#267f8c;
  --ink:#222222;
  --text:#555555;
  --white:#ffffff;
  --black:#1b1b1b;
  --blue:#2d7dc0;
  --green:#27ad5f;
  --gold:#efc416;
  --red:#c0392b;
  --footer:#1d1d1d;
}
*{box-sizing:border-box;margin:0;padding:0}
html,body{width:1200px;height:2791px;overflow:hidden}
body{position:relative;font-family:"Open Sans",Arial,sans-serif;color:var(--text);background:var(--white)}
h1,h2,h3{font-weight:400}
.abs{position:absolute}

/* header */
.topline{left:0;top:0;width:1200px;height:7px;background:var(--teal)}
.header{left:0;top:7px;width:1200px;height:118px;background:var(--white)}
.brand{left:102px;top:44px;display:flex;align-items:center;gap:12px}
.brand-mark{width:34px;height:34px;background:var(--teal-dark)}
.brand-name{font-weight:700;font-size:38px;color:var(--ink);letter-spacing:-1px}
.nav{top:54px;font-size:14px;font-weight:600;color:var(--ink)}
.btn-login,.btn-signin{top:47px;height:39px;width:80px;border-radius:4px;color:var(--white);font-size:14px;display:flex;align-items:center;justify-content:center}
.btn-login{left:925px;background:var(--black)}
.btn-signin{left:1019px;background:var(--teal)}

/* hero */
.hero{left:0;top:125px;width:1200px;height:545px;
  background:
    radial-gradient(ellipse 420px 300px at 600px 360px,rgba(70,60,50,.35),rgba(70,60,50,0)),
    linear-gradient(100deg,#93cfcc 0%,#a8c3a6 30%,#b5a879 60%,#a48a4f 100%)}
.hero-controls{left:0;top:125px;width:1200px;height:545px}

/* welcome */
.welcome-title{left:0;top:690px;width:1200px;text-align:center;font-size:28px;font-weight:600;color:var(--ink)}
.welcome-title span{color:var(--teal)}
.welcome-text{left:122px;top:740px;width:956px;text-align:center;font-size:12.2px;line-height:17.6px;color:var(--text)}

.feature{top:876px;width:306px;height:224px;background:linear-gradient(#f4f4f4,#e2e2e2)}
.feature-head{height:50px;background:var(--teal);color:var(--white);display:flex;align-items:center;gap:10px;padding-left:14px;font-size:16px;font-weight:600}
.feature-body{padding:14px 14px 0 16px;font-size:12.3px;line-height:24px;color:var(--text)}
.read-more{position:absolute;right:0;bottom:0;width:134px;height:41px;background:var(--teal);color:var(--white);font-size:13px;display:flex;align-items:center;justify-content:center}

/* services */
.services{left:0;top:1138px;width:1200px;height:518px;background:var(--teal)}
.services-title{left:99px;top:1168px;font-size:30px;font-weight:400;color:var(--white)}
.service-media{top:1224px;width:318px;height:143px}
.service-title{top:1437px;font-size:16px;font-weight:600;color:var(--white)}
.service-text{top:1467px;width:318px;font-size:11.5px;line-height:23px;color:var(--white)}
.more-info{top:1574px;width:98px;height:33px;background:var(--black);color:var(--white);font-size:11px;font-weight:600;display:flex;align-items:center;justify-content:center}

/* pricing */
.pricing{left:0;top:1656px;width:1200px;height:569px;background:linear-gradient(160deg,#f6f6f6,#ececec)}
.pricing-title{left:0;top:1683px;width:1200px;text-align:center;font-family:"Ubuntu",sans-serif;font-size:29px;font-weight:400;color:var(--teal)}
.plan{top:1745px;width:309px;height:417px;background:var(--white);border:1px solid #d0d0d0;border-radius:6px;overflow:hidden}
.plan-head{height:65px;color:var(--white);font-family:"Ubuntu",sans-serif;font-size:23px;font-weight:500;display:flex;align-items:center;justify-content:center}
.plan-price{position:absolute;left:100px;top:93px;width:108px;height:108px;border-radius:50%;background:var(--red);border:4px solid #f2d0cc;color:var(--white);text-align:center;font-family:"Ubuntu",sans-serif}
.plan-price b{display:block;margin-top:24px;font-size:27px;font-weight:500;line-height:30px}
.plan-price b sup{font-size:13px;vertical-align:10px}
.plan-price small{font-size:11px}
.plan-list{position:absolute;left:0;top:210px;width:100%;list-style:none;text-align:center;font-size:14px;line-height:29.5px;color:#444}
.plan-cta{position:absolute;left:0;bottom:0;width:100%;height:62px;background:var(--black);color:var(--white);font-family:"Ubuntu",sans-serif;font-size:17px;font-weight:500;display:flex;align-items:center;justify-content:center}

/* contact */
.contact{left:0;top:2225px;width:1200px;height:467px;background:linear-gradient(180deg,#6c7b84 0%,#8a969c 40%,#5d6a70 100%)}
.contact-title{left:0;top:2256px;width:1200px;text-align:center;font-size:28px;font-weight:400;color:var(--white)}
.field{left:100px;width:402px;background:var(--white);font-size:13px;color:#999;padding:14px 14px}
.submit{left:100px;top:2605px;width:402px;height:45px;background:var(--black);border-radius:3px;color:var(--white);font-size:14px;display:flex;align-items:center;justify-content:center}
.map{left:560px;top:2324px;width:541px;height:326px;background:linear-gradient(135deg,#ebe6c8,#e3dfd2 50%,#efe7b8)}

/* footer */
.footer{left:0;top:2692px;width:1200px;height:99px;background:var(--footer)}
.copyright{left:99px;top:2733px;font-size:14px;color:var(--white)}
.social{top:2725px;width:33px;height:33px}
</style>
</head>
<body>

<div class="abs topline"></div>
<header class="abs header"></header>
<div class="abs brand"><span class="brand-mark"></span><span class="brand-name">Lumavault</span></div>
<nav>
  <a class="abs nav" style="left:595px">Why Lumavault?</a>
  <a class="abs nav" style="left:725px">Pricing</a>
  <a class="abs nav" style="left:790px">About</a>
  <a class="abs nav" style="left:852px">Connect</a>
</nav>
<a class="abs btn-login">Login</a>
<a class="abs btn-signin">Sign In</a>

<section class="abs hero" role="img" aria-label="Slide illustration: a businessman meditating beneath an arc of four steps – consider your suitability, idea, market, and success your business"></section>
<svg class="abs hero-controls" width="1200" height="545" viewBox="0 0 1200 545">
  <path d="M58 260 L42 275 L58 290" fill="none" stroke="#fff" stroke-width="6"/>
  <path d="M1140 260 L1156 275 L1140 290" fill="none" stroke="#fff" stroke-width="6"/>
  <circle cx="577" cy="510" r="6" fill="none" stroke="#fff" stroke-width="2"/>
  <circle cx="599" cy="510" r="6" fill="#fff"/>
  <circle cx="621" cy="510" r="6" fill="#fff"/>
</svg>

<h1 class="abs welcome-title">Welcome To <span>Lumavault</span></h1>
<p class="abs welcome-text">Many services now exist for sharing your personal or corporate information online. The question is whether or not your information is secure and protected, and how much control you have over the information you share. Lumavault was established specifically to address this concern. Our Mission is to provide secure messaging channels to allow individuals, businesses, institutions and governments to securely communicate with their collaborators. Our service uses the strongest available encryption and proprietary technology to protect messages from eavesdroppers while offering users specific levels of control over their information, even after their emails, sms' and documents have been shared.</p>

<div class="abs feature" style="left:99px">
  <div class="feature-head">
    <svg width="26" height="26" viewBox="0 0 26 26"><path d="M4 22 L16 10 M10 4 L22 16" stroke="#fff" stroke-width="4" stroke-linecap="round"/><circle cx="18" cy="8" r="5" fill="none" stroke="#fff" stroke-width="3"/></svg>
    TURNKEY SOLUTION</div>
  <p class="feature-body">Our print program is one of the many solutions to consider for you business makeover. It is cost effective and easy for your business to learn and use. Fen and Rowe makes your business, our business.</p>
  <span class="read-more">Read more</span>
</div>
<div class="abs feature" style="left:445px">
  <div class="feature-head">
    <svg width="26" height="26" viewBox="0 0 26 26"><rect x="7" y="3" width="12" height="7" fill="#fff"/><rect x="2" y="10" width="22" height="10" rx="2" fill="#fff"/><rect x="7" y="16" width="12" height="8" fill="#fff" stroke="#2f9cac" stroke-width="2"/></svg>
    TECHNICAL SUPPORT</div>
  <p class="feature-body">Would you like to save money, improve efficiency and increase production? Fen and Rowe is your organization's resource when you look for a balance of multifunction systems and printers.</p>
  <span class="read-more">Read more</span>
</div>
<div class="abs feature" style="left:793px">
  <div class="feature-head">
    <svg width="24" height="24" viewBox="0 0 24 24"><circle cx="12" cy="12" r="5" fill="#fff"/><path d="M12 1v4M12 19v4M1 12h4M19 12h4M4 4l3 3M17 17l3 3M4 20l3-3M17 7l3-3" stroke="#fff" stroke-width="2"/></svg>
    WORLDWIDE PRESENCE</div>
  <p class="feature-body">Saving on postage is just one of the reasons to get a meter. In addition to the benefits listed below, postage meters help make your life simple. So, what are you waiting for?</p>
  <span class="read-more">Read more</span>
</div>

<section class="abs services"></section>
<h2 class="abs services-title">Services</h2>
<div class="abs service-media" style="left:99px;background:linear-gradient(90deg,#3a0a0e,#1b3f63 55%,#0c1d33)" role="img" aria-label="Digital artwork of glowing padlocks in red and blue"></div>
<div class="abs service-media" style="left:439px;background:linear-gradient(180deg,#3c5f86,#1d2c44 70%,#0e1522)" role="img" aria-label="Photo of hands holding a laptop with network devices floating above"></div>
<div class="abs service-media" style="left:781px;background:linear-gradient(120deg,#d9dde0,#a9b3bb 50%,#e9ecee)" role="img" aria-label="Photo of two business people working together at a laptop"></div>
<h3 class="abs service-title" style="left:99px">Content Security</h3>
<h3 class="abs service-title" style="left:439px">Network Protection</h3>
<h3 class="abs service-title" style="left:781px">Business Efficiency</h3>
<p class="abs service-text" style="left:99px">Lumavault uses the Advanced Encryption Standard (AES) with a 256 bit key to protect your content. This means that Lumavault provides the highest level of protection available to safeguard your information.</p>
<p class="abs service-text" style="left:439px">To ensure that your online networking environment is safe, Lumavault uses an Extended Validation Secure Socket Layer (EVSSL) certificate. That means that Lumavault has passed a rigorous identity</p>
<p class="abs service-text" style="left:781px">In today's world, being able to respond quickly, at anytime and from anywhere, can mean the difference between success and failure. This is why Lumavault offers an uptime SLA of 99.95%.</p>
<span class="abs more-info" style="left:99px">More info</span>
<span class="abs more-info" style="left:439px">More info</span>
<span class="abs more-info" style="left:781px">More info</span>

<section class="abs pricing"></section>
<h2 class="abs pricing-title">Pricing information</h2>
<div class="abs plan" style="left:99px">
  <div class="plan-head" style="background:var(--blue)">Per Package</div>
  <div class="plan-price"><b><sup>$</sup>8.14</b><small>Per month</small></div>
  <ul class="plan-list"><li>Package Processing $1</li><li>Payment Processing 4% of shipping costs</li><li>Package Consolidation starting from $2</li><li>Storage $1 add a tooltip</li></ul>
  <span class="plan-cta">Sign Up Now</span>
</div>
<div class="abs plan" style="left:450px">
  <div class="plan-head" style="background:var(--green)">Silver Plan</div>
  <div class="plan-price"><b><sup>$</sup>8.14</b><small>Per month</small></div>
  <ul class="plan-list"><li>Package Processing $1</li><li>Payment Processing 4% of shipping costs</li><li>Package Consolidation starting from $2</li><li>Storage $1 add a tooltip</li></ul>
  <span class="plan-cta">Sign Up Now</span>
</div>
<div class="abs plan" style="left:791px">
  <div class="plan-head" style="background:var(--gold)">Gold Plan</div>
  <div class="plan-price"><b><sup>$</sup>8.14</b><small>Per month</small></div>
  <ul class="plan-list"><li>Package Processing $1</li><li>Payment Processing 4% of shipping costs</li><li>Package Consolidation starting from $2</li><li>Storage $1 add a tooltip</li></ul>
  <span class="plan-cta">Sign Up Now</span>
</div>

<section class="abs contact" role="img" aria-label="Blurred photo of a city street used as background"></section>
<h2 class="abs contact-title">Contact Us</h2>
<div class="abs field" style="top:2324px;height:54px">Your Name</div>
<div class="abs field" style="top:2396px;height:54px">Your Email</div>
<div class="abs field" style="top:2469px;height:121px">Message</div>
<span class="abs submit">Submit</span>
<div class="abs map" role="img" aria-label="Street map showing the office location"></div>

<footer class="abs footer"></footer>
<p class="abs copyright">© 2014 Lumavault All Rights Reserved</p>
<span class="abs social" style="left:917px;background:#3b5b98"></span>
<span class="abs social" style="left:966px;background:#2aa3d8"></span>
<span class="abs social" style="left:1016px;background:#8c8c8c"></span>
<span class="abs social" style="left:1066px;background:#1f77b0"></span>

</body>
</html>
```